Fitness competition business needs a card design

I need a professional business card design using my logo. The card will be horizontal with rounded edges.

Target Market(s)

Female fitness competitors

Industry/Entity Type

Fitness

Contact Information for Business Card

Lise-Anne Korvath
Owner
stagevelora.com
210.555.0137
info@stagevelora.com

Font styles to use
Serif

Colors

Designer to choose colors to be used in the design.

Requirements
Must have
• On the back please add the following:
• Figure
• Bikini
• Physique
• Fitness
Nice to have
• Looking for a very sleek design, contemporary and easy to read.
Should not have
• Should not be difficult to read or be too busy

```html
<!DOCTYPE html>
<html lang="en">
<head>
<meta charset="utf-8">
<title>Stage Velora — Business Card</title>
<link rel="stylesheet" href="https://fonts.googleapis.com/css2?family=Tinos:wght@400;700&display=swap">
<style>
  :root {
    --backdrop: #1f1f21;
    --card-grey: #5e5e60;
    --card-white: #ffffff;
    --brand-red: #e0262b;
    --ink-grey: #4a4a4c;
    --soft-white: #f2f2f2;
    --photo-warm-a: #c98a6a;
    --photo-warm-b: #7a7a7c;
    --photo-cool-a: #f4f4f4;
    --photo-cool-b: #b9c8db;
  }
  * { box-sizing: border-box; margin: 0; padding: 0; }
  html, body {
    width: 1200px; height: 800px; overflow: hidden;
    background: var(--backdrop);
    font-family: "Tinos", "Times New Roman", serif;
  }
  .canvas { position: relative; width: 1200px; height: 800px; }
  .card {
    position: absolute; left: 300px; width: 600px; height: 343px;
    border-radius: 14px; overflow: hidden;
  }
  .card--back { top: 38px; background: var(--card-grey); }
  .card--front { top: 419px; background: var(--card-white); }

  .brand {
    position: absolute; z-index: 1; display: flex; align-items: center; gap: 10px;
    font-weight: 700; letter-spacing: 1px; text-transform: uppercase; white-space: nowrap;
  }
  .brand__dot { width: 18px; height: 18px; border-radius: 50%; flex: none; }
  .card--back .brand { left: 44px; top: 132px; font-size: 28px; color: var(--soft-white); }
  .card--back .brand__dot { background: var(--soft-white); }
  .card--front .brand { left: 40px; top: 74px; font-size: 26px; color: var(--brand-red); }
  .card--front .brand__dot { background: var(--brand-red); }

  .back__categories {
    position: absolute; left: 46px; top: 196px;
    color: var(--soft-white); font-size: 12px; letter-spacing: 1px; text-transform: uppercase;
    white-space: nowrap;
  }
  .back__web {
    position: absolute; left: 46px; top: 250px;
    color: var(--soft-white); font-size: 15px; letter-spacing: 4px;
  }

  .photo { position: absolute; top: 0; bottom: 0; right: 0; }
  .photo--athlete {
    width: 270px;
    background: radial-gradient(ellipse at 55% 45%, var(--photo-warm-a) 0%, #8e6a5c 35%, var(--photo-warm-b) 75%);
  }
  .photo--duo {
    width: 290px;
    background: radial-gradient(ellipse at 50% 55%, var(--photo-cool-b) 0%, #d9c5b4 40%, var(--photo-cool-a) 80%);
  }

  .person { position: absolute; left: 42px; top: 176px; }
  .person__name { color: var(--brand-red); font-size: 26px; }
  .person__role { color: var(--ink-grey); font-size: 15px; margin-top: 2px; }
  .rule {
    position: absolute; left: 42px; top: 234px; width: 250px; height: 1px;
    background: var(--brand-red);
  }
  .contact { position: absolute; left: 42px; top: 248px; list-style: none; }
  .contact__item {
    display: flex; align-items: center; gap: 10px;
    color: var(--ink-grey); font-size: 15px; height: 26px;
  }
  .contact__icon { width: 18px; height: 18px; flex: none; }
</style>
</head>
<body>
<main class="canvas">
  <section class="card card--back" aria-label="Card back">
    <div class="brand"><span class="brand__dot"></span>Stage Velora</div>
    <p class="back__categories">Figure · Bikini · Physique · Fitness</p>
    <p class="back__web">stagevelora.com</p>
    <div class="photo photo--athlete" role="img" aria-label="Photo of a female fitness competitor in an orange sports top, arms raised"></div>
  </section>

  <section class="card card--front" aria-label="Card front">
    <div class="brand"><span class="brand__dot"></span>Stage Velora</div>
    <div class="person">
      <p class="person__name">Lise-Anne Korvath</p>
      <p class="person__role">Owner</p>
    </div>
    <div class="rule"></div>
    <ul class="contact">
      <li class="contact__item">
        <svg class="contact__icon" viewBox="0 0 18 18" aria-hidden="true">
          <circle cx="9" cy="9" r="8.5" fill="none" stroke="var(--brand-red)" stroke-width="1.2"/>
          <path d="M6 5.2 L7.4 5 L8.2 7 L7.3 7.8 Q8 9.6 10.2 10.7 L11 9.8 L13 10.6 L12.8 12 Q8 12.6 5.4 7.2 Z" fill="var(--brand-red)"/>
        </svg>210.555.0137</li>
      <li class="contact__item">
        <svg class="contact__icon" viewBox="0 0 18 18" aria-hidden="true">
          <circle cx="9" cy="9" r="8.5" fill="none" stroke="var(--brand-red)" stroke-width="1.2"/>
          <rect x="4.8" y="6" width="8.4" height="6" fill="var(--brand-red)"/>
          <path d="M4.8 6 L9 9.4 L13.2 6" fill="none" stroke="#fff" stroke-width="0.9"/>
        </svg>info@stagevelora.com</li>
      <li class="contact__item">
        <svg class="contact__icon" viewBox="0 0 18 18" aria-hidden="true">
          <circle cx="9" cy="9" r="8.5" fill="none" stroke="var(--brand-red)" stroke-width="1.2"/>
          <circle cx="9" cy="9" r="4.6" fill="none" stroke="var(--brand-red)" stroke-width="1"/>
          <ellipse cx="9" cy="9" rx="2" ry="4.6" fill="none" stroke="var(--brand-red)" stroke-width="0.9"/>
          <path d="M4.4 9 H13.6" stroke="var(--brand-red)" stroke-width="0.9"/>
        </svg>stagevelora.com</li>
    </ul>
    <div class="photo photo--duo" role="img" aria-label="Photo of a male trainer in a blue shirt holding a clipboard beside a female athlete lifting blue dumbbells"></div>
  </section>
</main>
</body>
</html>
```